Tenbrook Business Card Design

We are the largest used car company fro JapanJust need a simple business cards to start with

Industry/Entity Type

Used Car

Contact Information for Business Card

Haruna " Ned" Morikawa
Operations Director
Tenbrook Australia Pty.Ltd.
P.O.Box 517 Pendlestone NSW 2093
M: 0466 518 274
P: 1800 574 392
email : haruna.morikawa@tnbk.co.jp

```html
<!DOCTYPE html>
<html lang="en">
<head>
<meta charset="utf-8">
<title>Tenbrook Business Card Design</title>
<link rel="stylesheet" href="https://fonts.googleapis.com/css2?family=Lato:wght@400;700&display=swap">
<style>
  :root {
    --backdrop: #ececec;
    --paper: #fbfbfb;
    --brand-orange: #e5472a;
    --brand-orange-light: #ef5a2c;
    --ink: #4a4a4a;
    --white: #ffffff;
    --shadow: rgba(0, 0, 0, 0.12);
  }
  * { box-sizing: border-box; margin: 0; padding: 0; }
  html, body {
    width: 1200px;
    height: 900px;
    overflow: hidden;
    background: var(--backdrop);
    font-family: "Lato", Arial, sans-serif;
  }
  .card-set {
    position: relative;
    width: 1200px;
    height: 900px;
  }
  .card {
    position: absolute;
    top: 297px;
    width: 500px;
    height: 306px;
    box-shadow: 0 6px 18px var(--shadow);
  }
  .card--front {
    left: 70px;
    background: var(--paper);
  }
  .card--back {
    left: 630px;
    background: radial-gradient(circle at 50% 40%, var(--brand-orange-light), var(--brand-orange) 70%);
    display: flex;
    align-items: center;
    justify-content: center;
  }
  .holder {
    position: absolute;
    left: 34px;
    top: 34px;
  }
  .holder__name {
    color: var(--brand-orange);
    font-weight: 700;
    font-size: 21px;
    line-height: 1.1;
  }
  .holder__role {
    color: var(--ink);
    font-size: 13px;
    margin-top: 2px;
  }
  .contact {
    position: absolute;
    left: 34px;
    top: 118px;
    list-style: none;
    font-size: 14px;
    line-height: 1.15;
  }
  .contact__item { margin-bottom: 4px; }
  .contact__label {
    display: block;
    color: var(--brand-orange);
    font-size: 13px;
  }
  .contact__value {
    display: block;
    color: var(--ink);
  }
  .wordmark {
    display: flex;
    align-items: center;
    gap: 10px;
    font-weight: 700;
    text-transform: uppercase;
    letter-spacing: 2px;
  }
  .wordmark__dot {
    width: 14px;
    height: 14px;
    border-radius: 50%;
  }
  .card--front .wordmark {
    position: absolute;
    right: 38px;
    top: 178px;
    color: var(--brand-orange);
    font-size: 34px;
  }
  .card--front .wordmark__dot { background: var(--brand-orange); }
  .card--back .wordmark {
    color: var(--white);
    font-size: 44px;
  }
  .card--back .wordmark__dot {
    background: var(--white);
    width: 18px;
    height: 18px;
  }
</style>
</head>
<body>
  <main class="card-set">
    <section class="card card--front" aria-label="Business card front">
      <header class="holder">
        <p class="holder__name">Dorian Pell</p>
        <p class="holder__role">Managing Director</p>
      </header>
      <ul class="contact">
        <li class="contact__item">
          <span class="contact__label">telephone</span>
          <span class="contact__value">044-987 612 305</span>
        </li>
        <li class="contact__item">
          <span class="contact__label">email</span>
          <span class="contact__value">hello@tnbkmail.com</span>
        </li>
        <li class="contact__item">
          <span class="contact__label">address</span>
          <span class="contact__value">2345, address goes here, country</span>
        </li>
      </ul>
      <div class="wordmark">
        <span class="wordmark__dot"></span>
        <span class="wordmark__name">Tenbrook</span>
      </div>
    </section>

    <section class="card card--back" aria-label="Business card back">
      <div class="wordmark">
        <span class="wordmark__dot"></span>
        <span class="wordmark__name">Tenbrook</span>
      </div>
    </section>
  </main>
</body>
</html>
```